Financial Planning business needs a new Business Card design

We need a business card design for an Australian financial planning business. I am looking for a clean simple design

Target Market(s)

People aged 25-40

Industry/Entity Type

Financial Service

Contact Information for Business Card

On the front of the card we need the following information:
Name: Colin Merrow (First Name Green: #006838 and last name Grey: #414042)
Position: Financial Adviser
Qualifications: BEc(Hons), AdDipFS(FP), Dip FMBM, CFL®
Mobile: 0437 512 604
Email: colin@brightledgeplan.com.au

On the back of the card we need:
Postal address: PO BOX 5307, PERTH BC, WA 6849
Website: www.brightledgeplan.com.au
Text: AFS Licence No. 518760

The fields need to be able to be edited.

Font styles to use
Sans Serif

Requirements
Must have
• Information listed above

```html
<!DOCTYPE html>
<html lang="en">
<head>
<meta charset="utf-8">
<title>Brightledge Business Card</title>
<link href="https://fonts.googleapis.com/css2?family=Roboto+Condensed:wght@400;700&display=swap" rel="stylesheet">
<style>
  :root {
    --green: #006838;
    --grey: #414042;
    --charcoal: #47474b;
    --white: #ffffff;
    --stage: #efeeec;
    --muted: #6c6c70;
    --text-font: "Roboto Condensed", "Arial Narrow", sans-serif;
  }
  * { margin: 0; padding: 0; box-sizing: border-box; }
  html, body { width: 1200px; height: 465px; overflow: hidden; background: var(--stage); }
  .stage { position: relative; width: 1200px; height: 465px; }
  .card {
    position: absolute;
    background: var(--white);
    overflow: hidden;
    box-shadow: 0 4px 14px rgba(0,0,0,0.18);
    font-family: var(--text-font);
  }
  .card-front { left: 22px; top: 58px; width: 545px; height: 330px; }
  .card-back  { left: 592px; top: 78px; width: 530px; height: 330px; }
  .card-waves { position: absolute; inset: 0; width: 100%; height: 100%; }
  .brand-name {
    position: absolute;
    font-weight: 700;
    color: var(--green);
    letter-spacing: 0.5px;
    white-space: nowrap;
    line-height: 1;
  }
  .card-front .brand-name { left: 28px; top: 82px; font-size: 56px; }
  .card-back .brand-name { right: 40px; top: 80px; font-size: 56px; }
  .card-back .brand-name-faint {
    left: 24px; top: 228px; right: auto; font-size: 24px; color: var(--muted);
  }
  .person-name {
    position: absolute; right: 20px; top: 156px;
    font-size: 22px; line-height: 26px; white-space: nowrap;
  }
  .first-name { color: var(--green); }
  .last-name { color: var(--grey); }
  .person-role { font-size: 15px; color: var(--grey); }
  .contact-block {
    position: absolute; right: 20px; top: 244px;
    text-align: right; color: var(--white);
  }
  .qualifications { font-size: 15px; line-height: 18px; white-space: nowrap; }
  .contact-line {
    display: flex; justify-content: flex-end; align-items: center; gap: 8px;
    font-size: 14.5px; line-height: 18px; margin-top: 9px; white-space: nowrap;
  }
  .contact-line svg { width: 12px; height: 12px; fill: var(--white); }
  .licence {
    position: absolute; right: 42px; top: 142px;
    font-size: 15px; color: var(--grey);
  }
  .back-details { position: absolute; left: 26px; top: 268px; color: var(--white); }
  .back-line { display: flex; align-items: center; gap: 9px; font-size: 15px; line-height: 18px; margin-bottom: 10px; white-space: nowrap; }
  .back-line svg { width: 13px; height: 13px; fill: var(--white); }
</style>
</head>
<body>
<main class="stage">

  <section class="card card-front" aria-label="Business card front">
    <svg class="card-waves" viewBox="0 0 545 330" preserveAspectRatio="none" aria-hidden="true">
      <path d="M0,210 C170,262 320,198 545,186 L545,196 C320,212 170,284 0,252 Z" fill="var(--grey)"/>
      <path d="M0,262 C170,290 300,212 545,202 L545,330 L0,330 Z" fill="var(--green)"/>
    </svg>
    <div class="brand-name">BRIGHTLEDGE</div>
    <p class="person-name"><span class="first-name">Colin</span> <span class="last-name">Merrow,</span> <span class="person-role">Financial Adviser</span></p>
    <div class="contact-block">
      <p class="qualifications">BEc(Hons), AdDipFS(FP) Dip FMBM, CFL®</p>
      <p class="contact-line">0437 512 604
        <svg viewBox="0 0 12 12"><path d="M3,0 H9 V12 H3 Z M4,1.5 V9 H8 V1.5 Z"/></svg>
      </p>
      <p class="contact-line">colin@brightledgeplan.com.au
        <svg viewBox="0 0 12 12"><path d="M0,3 L6,7 L12,3 V11 H0 Z M0,1.5 H12 L6,5.5 Z"/></svg>
      </p>
    </div>
  </section>

  <section class="card card-back" aria-label="Business card back">
    <svg class="card-waves" viewBox="0 0 530 330" preserveAspectRatio="none" aria-hidden="true">
      <path d="M0,192 C140,150 300,222 530,184 L530,330 L0,330 Z" fill="var(--charcoal)"/>
      <path d="M0,173 C140,135 300,205 530,166" fill="none" stroke="var(--green)" stroke-width="5"/>
    </svg>
    <div class="brand-name">BRIGHTLEDGE</div>
    <p class="licence">AFS Licence No. 518760</p>
    <div class="brand-name brand-name-faint">BRIGHTLEDGE</div>
    <div class="back-details">
      <p class="back-line">
        <svg viewBox="0 0 12 12"><path d="M6,0 C3,0 1.5,2 1.5,4.3 C1.5,7 6,12 6,12 C6,12 10.5,7 10.5,4.3 C10.5,2 9,0 6,0 Z M6,2.5 A1.8,1.8 0 1 1 6,6.1 A1.8,1.8 0 1 1 6,2.5 Z"/></svg>
        PO BOX 5307, PERTH BC, WA 6849
      </p>
      <p class="back-line">
        <svg viewBox="0 0 12 12"><circle cx="6" cy="6" r="5.2" fill="none" stroke="var(--white)" stroke-width="1.2"/><path d="M0.8,6 H11.2 M6,0.8 C3.5,3.5 3.5,8.5 6,11.2 M6,0.8 C8.5,3.5 8.5,8.5 6,11.2" fill="none" stroke="var(--white)" stroke-width="1"/></svg>
        www.brightledgeplan.com.au
      </p>
    </div>
  </section>

</main>
</body>
</html>
```